Company Profile for Consulting Comany

Need Company profile to be designed in a professional way.

for inspiring :-
https://www.vimolia.net/gallery/5307462/COMPANY-PROFILE
https://www.vimolia.net/gallery/20934617/Biotech-Product-Catalog-No1-(Laminar-Air-Flow)
https://www.vimolia.net/gallery/38720954/RKT-Tramvale-Company-Profile-2014-(RKT-Rebrand-part-2)

Target Market(s)

Corporate

Industry/Entity Type

It Company

Font styles to use
Sans Serif

Requirements
Must have
• Landscape A4 size
• Must go with the logo branding
• Must Have Visual Identity is the most important
• Must Have mpty spaces

```html
<!DOCTYPE html>
<html lang="en">
<head>
<meta charset="utf-8">
<title>Shiftpoint Advisory — Profile Covers</title>
<link rel="stylesheet" href="https://fonts.googleapis.com/css2?family=Oswald:wght@600&family=Roboto:wght@400;500;700&display=swap">
<style>
  :root {
    --page: #ffffff;
    --ink-dark: #111214;
    --photo-light: #5a5c60;
    --photo-dark: #0c0d0f;
    --brand-blue: #1ea1cf;
    --brand-blue-deep: #127fa8;
    --band-text: #0b2a3a;
    --body-text: #2a2a2a;
    --rule: #3a3a3a;
    --white: #ffffff;
  }
  * { margin: 0; padding: 0; box-sizing: border-box; }
  html, body { width: 848px; height: 1200px; overflow: hidden; background: var(--page); }
  body { position: relative; font-family: "Roboto", Arial, sans-serif; color: var(--body-text); }

  .cover { position: absolute; left: 59px; width: 717px; height: 509px; overflow: hidden; background: var(--white); }
  .cover--front { top: 71px; }
  .cover--back { top: 608px; }

  .photo { position: absolute; left: 0; top: 0; width: 100%; }
  .cover--front .photo {
    height: 452px;
    background: radial-gradient(ellipse at 50% 70%, #6b6d70 0%, #3a3c40 40%, var(--photo-dark) 100%);
  }
  .cover--back .photo {
    height: 127px;
    background: linear-gradient(90deg, #1a1b1d 0%, #55575b 45%, #4a4c50 60%, #141517 100%);
  }

  .brand-box {
    position: absolute; left: 50%; transform: translateX(-50%);
    background: var(--ink-dark);
    display: flex; flex-direction: column; align-items: center; justify-content: center;
    gap: 10px; text-align: center;
  }
  .cover--front .brand-box { top: 0; width: 198px; height: 191px; }
  .cover--back .brand-box { top: 71px; width: 140px; height: 148px; gap: 8px; }
  .brand-box__mark { width: 26px; height: 26px; background: var(--brand-blue); }
  .cover--back .brand-box__mark { width: 20px; height: 20px; }
  .brand-box__name {
    color: var(--brand-blue); font-weight: 500; font-size: 27px; line-height: 1.05;
  }
  .cover--back .brand-box__name { font-size: 19px; }

  .headline { position: absolute; left: 0; width: 100%; text-align: center; color: var(--white); }
  .headline__lead { top: 294px; font-size: 26px; font-weight: 500; letter-spacing: 1px; }
  .headline__main { top: 330px; font-family: "Oswald", "Arial Narrow", sans-serif; font-weight: 600; font-size: 40px; letter-spacing: 0.5px; }

  .url-band {
    position: absolute; left: 0; width: 100%;
    background: linear-gradient(90deg, var(--brand-blue-deep) 0%, var(--brand-blue) 50%, var(--brand-blue-deep) 100%);
    display: flex; align-items: center; justify-content: center;
    color: var(--band-text); font-weight: 700; font-size: 18px;
  }
  .cover--front .url-band { top: 452px; height: 57px; }
  .cover--back .url-band { top: 459px; height: 50px; }

  .office { position: absolute; top: 254px; width: 215px; font-size: 10px; line-height: 1.35; }
  .office--dubai { left: 153px; }
  .office--khobar { left: 463px; }
  .office__city {
    display: inline-block; background: var(--brand-blue); color: var(--ink-dark);
    font-size: 11px; font-weight: 500; padding: 2px 8px 2px 10px; margin-bottom: 6px; margin-left: 13px;
  }
  .office__row { display: flex; gap: 6px; align-items: flex-start; margin-bottom: 5px; }
  .office__row svg { flex: none; width: 10px; height: 10px; margin-top: 1px; fill: var(--ink-dark); }
  .office__row--plain { padding-left: 16px; }

  .divider { position: absolute; left: 360px; top: 251px; width: 1px; height: 141px; background: var(--rule); }
</style>
</head>
<body>

<section class="cover cover--front">
  <div class="photo" role="img" aria-label="Black-and-white photo of a wooden boardwalk crossing sand dunes under a cloudy sky"></div>
  <div class="brand-box">
    <span class="brand-box__mark"></span>
    <span class="brand-box__name">Shiftpoint<br>Advisory</span>
  </div>
  <p class="headline headline__lead">WE CAN HELP YOU TO</p>
  <p class="headline headline__main">MAKE CHANGE HAPPEN</p>
  <div class="url-band">www.shiftpointadvisory.com</div>
</section>

<section class="cover cover--back">
  <div class="photo" role="img" aria-label="Dark misty forest with tall tree trunks"></div>
  <div class="brand-box">
    <span class="brand-box__mark"></span>
    <span class="brand-box__name">Shiftpoint<br>Advisory</span>
  </div>

  <div class="office office--dubai">
    <span class="office__city">DUBAI</span>
    <div class="office__row">
      <svg viewBox="0 0 10 10"><path d="M5 0.5 L10 5 H8.5 V9.5 H6 V6.5 H4 V9.5 H1.5 V5 H0 Z"/></svg>
      <span>PO BOX 48810, Dubai, UAE</span>
    </div>
    <div class="office__row office__row--plain">14th Floor, Harbour View Tower 3, Marlow Avenue.</div>
    <div class="office__row">
      <svg viewBox="0 0 10 10"><path d="M2 0.5 L4 2.5 L3 4 Q4.5 6 6 7 L7.5 6 L9.5 8 L8 9.5 Q3 9 0.5 2 Z"/></svg>
      <span>00971 4 555 0192</span>
    </div>
    <div class="office__row">
      <svg viewBox="0 0 10 10"><path d="M2.5 0.5 H7.5 V3.5 H2.5 Z M0.5 4 H9.5 V8 H8 V9.5 H2 V8 H0.5 Z"/></svg>
      <span>00971 4 555 0193</span>
    </div>
    <div class="office__row">
      <svg viewBox="0 0 10 10"><path d="M0.5 2 H9.5 V8 H0.5 Z" /></svg>
      <span>info@shiftpointadvisory.com</span>
    </div>
  </div>

  <div class="divider"></div>

  <div class="office office--khobar">
    <span class="office__city">KHOBAR</span>
    <div class="office__row">
      <svg viewBox="0 0 10 10"><path d="M5 0.5 L10 5 H8.5 V9.5 H6 V6.5 H4 V9.5 H1.5 V5 H0 Z"/></svg>
      <span>PO BOX 27614, Khobar 31870,<br>SAUDI ARABIA</span>
    </div>
    <div class="office__row office__row--plain">9th Floor, Corniche Point Tower,<br>Palm Grove St.</div>
    <div class="office__row">
      <svg viewBox="0 0 10 10"><path d="M2 0.5 L4 2.5 L3 4 Q4.5 6 6 7 L7.5 6 L9.5 8 L8 9.5 Q3 9 0.5 2 Z"/></svg>
      <span>00966 13 555 0471</span>
    </div>
    <div class="office__row">
      <svg viewBox="0 0 10 10"><path d="M0.5 2 H9.5 V8 H0.5 Z" /></svg>
      <span>info@shiftpointadvisory.com</span>
    </div>
  </div>

  <div class="url-band">www.shiftpointadvisory.com</div>
</section>

</body>
</html>
```